Bonusheft für Patienten als kleine DIN A6 Broschüre
Zielgruppe
Bonusheft für Patienten als kleine DIN A6 Broschüre in der Zahn-Prophylaxe. Die Texte haben wir bereits vollständig formuliert, auch die Gliederung ist vorgegeben.
Wir sind eine Zahnarztpraxis mit dem Schwerpunkt Prophylaxe. Für unsere Prophylaxeabteilung möchten wir eine DIN A6 Broschüre entwerfen lassen, die als Bonusheft für Patienten dient.
Inhalt: Informationen über unsere Praxis, die leitende Mitarbeiterin, individuelle Risiken und Empfehlungen der Patienten. Auch Fakten und Tipps zur Verbesserung der Mundhygiene und Putzgewohnheiten werden Beschrieben.
Aufgabenstellung
Broschüre als DIN A6 Bonusheft mit circa sieben gestalteten Seiten, bei denen wir den Aufbau und die exakten Texte bereits vollständig vorgeben. Zusätzlich folgen mehrere gleiche Seiten, bei denen die Termine und Stempel eingetragen werden (ca. fünf Seiten).
Für Ihre Orientierung haben wir unsere Fotos und Farbschema von vorhandenen Designs unserer Praxis bereitgestellt.
Orientieren Sie sich gerne an unserer vorhandenen Homepage im Hinblick auf unseren Stil und das Praxislogo.
Homepage: www.zahnpraxis-am-lindenhof.de
Wir stellen einige Fotos zur Verwendung bereit. Falls nötig, verwenden Sie auch Stock Fotos.
Im folgenden werden wir den gewünschten Aufbau mit den Texten je Seite detailliert vorstellen. Ihre Aufgabe ist es, dies in ein modernes, frisches, ansprechendes und kompetentes Design umzusetzen.
1. Seite / Cover
- Mit Praxislogo
- Text: „Mein Prophylaxepass“
2. Seite:
- Überschrift: „Sie lassen nicht jeden an Ihre Zähne? Wir auch nicht.“
-Text: „Herzlich Willkommen! Mein Name ist Merle und ich arbeite als leitende Mitarbeiterin im Lindenhof Zentrum Bochum. Momentan befinde ich mich in der Weiterbildung zur Dentalhygienikerin und bin begeistert von der Arbeit in der präventiven Zahnmedizin. Mit meinem Wissen und meiner Erfahrung möchte ich dazu beitragen, dass unsere Patienten sich bei uns wohl und gut betreut fühlen. Ich freue mich darauf, Ihnen zu helfen, Ihre Zahngesundheit zu erhalten und zu verbessern!“
- Foto einer Mitarbeiterin
4. Seite:
- Überschrift: „Die professionelle Zahnreinigung – Wellness & Prävention“
- Text: „Eine wichtige Präventionsmaßnahme ist die regelmäßige Zahnreinigung in unserem Prophylaxe-Zentrum. Karies, Mundgeruch und Zahnfleischerkrankungen werden effektiv vorgebeugt. Die Zahnreinigung ist ein Teil der individuell geplanten Prophylaxe und eine sinnvolle Ergänzung der häus..

```html
<!DOCTYPE html>
<html lang="de">
<head>
<meta charset="utf-8">
<title>Mein Prophylaxepass – Zahnpraxis am Lindenhof</title>
<link href="https://fonts.googleapis.com/css2?family=Questrial&display=swap" rel="stylesheet">
<style>
:root{
  --taupe:#c2b99a;
  --frame:#c4bb9c;
  --gold-text:#c9bf9e;
  --field:#ececec;
  --band:#f4f3ef;
  --ink:#1e1e1e;
  --page-border:#c9c9c9;
  --white:#ffffff;
}
*{box-sizing:border-box;margin:0;padding:0}
html,body{width:1200px;height:815px;overflow:hidden;background:var(--white)}
body{position:relative;font-family:"Questrial",sans-serif;color:var(--ink)}

.page{position:absolute;background:var(--white);border:1px solid var(--page-border);overflow:hidden;box-shadow:1px 1px 2px rgba(0,0,0,.08)}
.pass-page{left:73px;top:68px;width:478px;height:678px}
.thumb{width:181px;height:257px}

/* ---------- appointment form (full size) ---------- */
.pass-header{position:absolute;font-size:15.5px;left:38px}
.pass-field{position:absolute;height:24px;background:var(--field);border-radius:6px}
.form-box{position:absolute;width:400px;height:165px;border:2px solid var(--frame);border-radius:14px;font-size:14.5px}
.form-box .tab{position:absolute;left:16px;top:-18px;width:228px;height:27px;background:var(--taupe);color:var(--white);border-radius:7px;font-size:21px;line-height:27px;padding-left:12px;letter-spacing:.3px}
.form-box .lbl{position:absolute;line-height:18px}
.form-box .fld{position:absolute;height:21px;background:var(--field);border-radius:4px}
.form-box .rule{position:absolute;left:0;right:0;height:2px;background:var(--frame)}
.form-box .opt{position:absolute;line-height:18px;padding-left:24px}
.form-box .opt::before{content:"";position:absolute;left:0;top:0;width:17px;height:17px;border:2px solid var(--frame);border-radius:50%}

.scaled{position:absolute;left:0;top:0;transform-origin:0 0}

/* ---------- thumbnail pages ---------- */
.head-band{position:absolute;left:0;top:0;width:100%;background:var(--band)}
.head-title{position:absolute;left:14px;top:12px;color:var(--gold-text);font-size:8px;line-height:10px}
.small-text{position:absolute;font-size:5.4px;line-height:7.9px}
.sub-title{position:absolute;color:var(--gold-text);font-size:6.2px}
.photo{position:absolute}
.check-list{position:absolute;list-style:none;font-size:5.6px}
.check-list li{position:relative;height:11.7px;line-height:8px;padding-left:10px}
.check-list li::before{content:"";position:absolute;left:0;top:0;width:7px;height:7px;border:1px solid var(--frame);border-radius:50%}

.cover-band{position:absolute;left:0;top:12px;width:100%;height:26px;background:var(--taupe);color:var(--white);font-size:10px;line-height:26px;text-align:center}
.brand{position:absolute;left:0;width:100%;text-align:center;color:#4a4a4a}
.brand .mark{display:block;width:12px;height:12px;margin:0 auto 3px;background:var(--taupe)}
.brand .name{display:block;font-size:10.5px;line-height:11px}
.brand .suffix{display:block;font-size:6.3px;line-height:8px}
.brand .team{display:block;font-size:3.4px;line-height:6px;margin-top:2px}

.hours{position:absolute;left:16px;font-size:5.8px;line-height:8.5px}
.hours td{padding-right:6px;vertical-align:top}
</style>
</head>
<body>

<!-- ================= Large appointment page ================= -->
<section class="page pass-page">
  <div class="pass-sheet">
    <p class="pass-header" style="top:34px">Prophylaxe Pass überreicht am:</p>
    <div class="pass-field" style="left:282px;top:36px;width:160px"></div>
    <p class="pass-header" style="top:72px">Mitarbeiterin:</p>
    <div class="pass-field" style="left:146px;top:70px;width:296px"></div>

    <div class="form-box" style="left:39px;top:149px">
      <div class="tab">Ihr nächster Termin:</div>
      <span class="lbl" style="left:16px;top:20px">Datum</span>
      <div class="fld" style="left:67px;top:18px;width:127px"></div>
      <span class="lbl" style="left:206px;top:20px">Uhrzeit</span>
      <div class="fld" style="left:258px;top:18px;width:127px"></div>
      <div class="rule" style="top:45px"></div>
      <span class="lbl" style="left:16px;top:56px">Intervall</span>
      <span class="opt" style="left:95px;top:56px">3 Monate</span>
      <span class="opt" style="left:229px;top:56px">6 Monate</span>
      <span class="opt" style="left:95px;top:80px">4 Monate</span>
      <span class="opt" style="left:229px;top:80px">12 Monate</span>
      <div class="rule" style="top:106px"></div>
      <span class="lbl" style="left:16px;top:116px">Terminart</span>
      <span class="opt" style="left:95px;top:116px">Regulärer Termin</span>
      <span class="opt" style="left:254px;top:116px">Kompakttermin</span>
      <span class="lbl" style="left:16px;top:141px">Behandelt von:</span>
      <div class="fld" style="left:121px;top:139px;width:259px"></div>
    </div>

    <div class="form-box" style="left:39px;top:389px">
      <div class="tab">Heutiger Termin:</div>
      <span class="lbl" style="left:16px;top:20px">Datum</span>
      <div class="fld" style="left:67px;top:18px;width:127px"></div>
      <span class="lbl" style="left:206px;top:20px">Uhrzeit</span>
      <div class="fld" style="left:258px;top:18px;width:127px"></div>
      <div class="rule" style="top:45px"></div>
      <span class="lbl" style="left:16px;top:56px">Intervall</span>
      <span class="opt" style="left:95px;top:56px">3 Monate</span>
      <span class="opt" style="left:229px;top:56px">6 Monate</span>
      <span class="opt" style="left:95px;top:80px">4 Monate</span>
      <span class="opt" style="left:229px;top:80px">12 Monate</span>
      <div class="rule" style="top:106px"></div>
      <span class="lbl" style="left:16px;top:116px">Terminart</span>
      <span class="opt" style="left:95px;top:116px">Regulärer Termin</span>
      <span class="opt" style="left:254px;top:116px">Kompakttermin</span>
      <span class="lbl" style="left:16px;top:141px">Behandelt von:</span>
      <div class="fld" style="left:121px;top:139px;width:259px"></div>
    </div>
  </div>
</section>

<!-- ================= Row 1 ================= -->
<section class="page thumb" style="left:622px;top:11px">
  <div class="photo" role="img" aria-label="Baumkronen vor blauem Himmel" style="left:0;top:0;width:100%;height:12px;background:linear-gradient(90deg,#9cc3dc,#6f9a6a)"></div>
  <div class="cover-band">Mein Prophylaxepass</div>
  <div class="photo" role="img" aria-label="Praxisgebäude aus rotem Backstein unter blauem Himmel" style="left:0;top:38px;width:100%;height:144px;background:linear-gradient(180deg,#7fb0dc 0%,#c9dcec 45%,#8a5440 62%,#6d7d5a 100%)"></div>
  <div class="brand" style="top:199px">
    <span class="mark"></span>
    <span class="name">Zahnpraxis</span>
    <span class="suffix">am Lindenhof</span>
    <span class="team">Dr. Jonas &amp; Lea Brandt mit Team</span>
  </div>
</section>

<section class="page thumb" style="left:813px;top:11px">
  <div class="head-band" style="height:43px"></div>
  <h2 class="head-title">Sie lassen nicht jeden an Ihre Zähne?<br>Wir auch nicht.</h2>
  <p class="sub-title" style="left:0;width:100%;text-align:center;top:51px">Herzlich Willkommen!</p>
  <div class="photo" role="img" aria-label="Porträt der leitenden Mitarbeiterin mit blondem Haar" style="left:14px;top:72px;width:66px;height:121px;border-radius:10px 0 0 0;background:linear-gradient(160deg,#dfe6ea,#c9b28c 55%,#2a3550)"></div>
  <p class="small-text" style="left:81px;top:66px;width:94px">Mein Name ist Merle und ich arbeite als leitende Mitarbeiterin im Lindenhof Zentrum Bochum.<br><br>Momentan befinde ich mich in der Weiterbildung zur Dentalhygienikerin und bin begeistert von der Arbeit in der präventiven Zahnmedizin. Mit meinem Wissen und meiner Erfahrung möchte ich dazu beitragen, dass unsere Patienten sich bei uns wohl und gut betreut fühlen.<br><br>Ich freue mich darauf, Ihnen zu helfen, Ihre Zahngesundheit zu erhalten und zu verbessern!</p>
</section>

<section class="page thumb" style="left:1005px;top:11px">
  <div class="head-band" style="height:43px"></div>
  <h2 class="head-title">Die professionelle Zahnreinigung –<br>Wellness &amp; Prävention</h2>
  <p class="small-text" style="left:14px;top:48px;width:158px">Eine wichtige Präventionsmaßnahme ist die regelmäßige Zahnreinigung in unserem Prophylaxe-Zentrum. Karies, Mundgeruch und Zahnfleischerkrankungen werden effektiv vorgebeugt. Die Zahnreinigung ist ein Teil der individuell geplanten Prophylaxe und eine sinnvolle Ergänzung der häuslichen Zahnpflege, gerade an den Stellen, wo die eigene Zahnbürste nicht hinkommt. Schonend werden alle harten und weichen Beläge von allen Zahnoberflächen entfernt — inklusive Kaffee-, Tee- und Raucherbelägen.</p>
  <div class="photo" role="img" aria-label="Lächelnder junger Mann mit Bart" style="left:0;top:152px;width:83px;height:105px;background:linear-gradient(160deg,#e4edf3,#b48a6a 55%,#1f2c3e)"></div>
  <p class="sub-title" style="left:90px;top:149px;font-size:5.4px">Natürlich weiße Zähne!</p>
  <p class="small-text" style="left:90px;top:161px;width:86px">Nach der professionellen Zahnreinigung stellt sich Ihre natürliche Zahnfarbe wieder ein und ein frisches Mundgefühl entsteht. In den meisten Fällen werden die Zähne nach der Prophylaxe heller. Erhöhen Sie Ihre Lebensqualität!</p>
</section>

<!-- ================= Row 2 ================= -->
<section class="page thumb" style="left:622px;top:279px">
  <div class="head-band" style="height:43px"></div>
  <h2 class="head-title">Moderne Technik für eine bessere<br>Behandlung</h2>
  <p class="small-text" style="left:14px;top:55px;width:76px">Für unsere Prophylaxebehandlungen nutzen wir aktuelle Behandlungsmethoden und bedienen uns neuer Technologie wie dem ClearJet® Prophylaxis Pro.</p>
  <p class="small-text" style="left:95px;top:55px;width:80px">Dadurch gewährleisten wir für unsere Patienten eine leise und angenehme Behandlung. Gleichzeitig stellen wir eine ausgezeichnete Behandlungsqualität sicher, welche Ihre Zähne nachhaltig schützt und Krankheiten vorbeugt.</p>
  <div class="photo" role="img" aria-label="Patientin im Gespräch mit einem Mitarbeiter, Orchideen im Vordergrund" style="left:0;top:147px;width:100%;height:110px;background:linear-gradient(100deg,#2e7f7c 0%,#7fb7c4 35%,#e9e4dc 60%,#8a6a55 100%)"></div>
</section>

<section class="page thumb" style="left:813px;top:279px">
  <div class="photo" role="img" aria-label="Familie mit Baby im Gespräch am Empfang" style="left:0;top:0;width:100%;height:108px;background:linear-gradient(110deg,#9fc6dc 0%,#e6eef2 40%,#273246 60%,#d9c6a8 100%)"></div>
  <div class="head-band" style="top:108px;height:25px"></div>
  <h2 class="head-title" style="top:116px">Risikoanalyse</h2>
  <ul class="check-list" style="left:28px;top:142px">
    <li>Kariesaktivität</li>
    <li>Empfindliches Zahnfleisch</li>
    <li>Erosionen / Säureschäden</li>
    <li>Zahnschmelzverlust</li>
    <li>Weicher Zahnschmelz</li>
    <li>Halitosis (Mundgeruch)</li>
    <li>Zahnverfärbungen</li>
    <li>Rauchen</li>
    <li>Retainer</li>
  </ul>
</section>

<section class="page thumb" style="left:1005px;top:279px">
  <div class="head-band" style="height:33px"></div>
  <h2 class="head-title">Ergänzende Pflegetipps</h2>
  <ul class="check-list" style="left:28px;top:42px">
    <li>Zahnseide</li>
    <li>Superfloss</li>
    <li>Zahnseidesticks</li>
    <li>Interdentalbürstchen</li>
    <li>Zungenreinigung</li>
    <li>Intensiv Fluoridierung</li>
    <li>1x wöchentliche Spezial Zahnpasta</li>
    <li>Mundddusche</li>
    <li>Mundspüllösung</li>
  </ul>
  <div class="photo" role="img" aria-label="Mitarbeiterin in grüner Praxiskleidung hält ein Zahnmodell" style="left:0;top:151px;width:100%;height:106px;background:radial-gradient(circle at 55% 55%,#9a9a9a,#5f5f5f 60%,#4a5a55)"></div>
</section>

<!-- ================= Row 3 ================= -->
<section class="page thumb" style="left:622px;top:547px">
  <div class="scaled" style="transform:scale(.379);width:478px;height:678px">
    <p class="pass-header" style="top:34px">Prophylaxe Pass überreicht am:</p>
    <div class="pass-field" style="left:282px;top:36px;width:160px"></div>
    <p class="pass-header" style="top:72px">Mitarbeiterin:</p>
    <div class="pass-field" style="left:146px;top:70px;width:296px"></div>
    <div class="form-box" style="left:39px;top:149px">
      <div class="tab">Ihr nächster Termin:</div>
      <span class="lbl" style="left:16px;top:20px">Datum</span><div class="fld" style="left:67px;top:18px;width:127px"></div>
      <span class="lbl" style="left:206px;top:20px">Uhrzeit</span><div class="fld" style="left:258px;top:18px;width:127px"></div>
      <div class="rule" style="top:45px"></div>
      <span class="lbl" style="left:16px;top:56px">Intervall</span>
      <span class="opt" style="left:95px;top:56px">3 Monate</span><span class="opt" style="left:229px;top:56px">6 Monate</span>
      <span class="opt" style="left:95px;top:80px">4 Monate</span><span class="opt" style="left:229px;top:80px">12 Monate</span>
      <div class="rule" style="top:106px"></div>
      <span class="lbl" style="left:16px;top:116px">Terminart</span>
      <span class="opt" style="left:95px;top:116px">Regulärer Termin</span><span class="opt" style="left:254px;top:116px">Kompakttermin</span>
      <span class="lbl" style="left:16px;top:141px">Behandelt von:</span><div class="fld" style="left:121px;top:139px;width:259px"></div>
    </div>
    <div class="form-box" style="left:39px;top:389px">
      <div class="tab">Heutiger Termin:</div>
      <span class="lbl" style="left:16px;top:20px">Datum</span><div class="fld" style="left:67px;top:18px;width:127px"></div>
      <span class="lbl" style="left:206px;top:20px">Uhrzeit</span><div class="fld" style="left:258px;top:18px;width:127px"></div>
      <div class="rule" style="top:45px"></div>
      <span class="lbl" style="left:16px;top:56px">Intervall</span>
      <span class="opt" style="left:95px;top:56px">3 Monate</span><span class="opt" style="left:229px;top:56px">6 Monate</span>
      <span class="opt" style="left:95px;top:80px">4 Monate</span><span class="opt" style="left:229px;top:80px">12 Monate</span>
      <div class="rule" style="top:106px"></div>
      <span class="lbl" style="left:16px;top:116px">Terminart</span>
      <span class="opt" style="left:95px;top:116px">Regulärer Termin</span><span class="opt" style="left:254px;top:116px">Kompakttermin</span>
      <span class="lbl" style="left:16px;top:141px">Behandelt von:</span><div class="fld" style="left:121px;top:139px;width:259px"></div>
    </div>
  </div>
</section>

<section class="page thumb" style="left:813px;top:547px">
  <div class="scaled" style="transform:scale(.38);width:478px;height:678px">
    <div class="form-box" style="left:38px;top:52px">
      <div class="tab">Weiterer Termin:</div>
      <span class="lbl" style="left:16px;top:20px">Datum</span><div class="fld" style="left:67px;top:18px;width:127px"></div>
      <span class="lbl" style="left:206px;top:20px">Uhrzeit</span><div class="fld" style="left:258px;top:18px;width:127px"></div>
      <div class="rule" style="top:45px"></div>
      <span class="lbl" style="left:16px;top:56px">Intervall</span>
      <span class="opt" style="left:95px;top:56px">3 Monate</span><span class="opt" style="left:229px;top:56px">6 Monate</span>
      <span class="opt" style="left:95px;top:80px">4 Monate</span><span class="opt" style="left:229px;top:80px">12 Monate</span>
      <div class="rule" style="top:106px"></div>
      <span class="lbl" style="left:16px;top:116px">Terminart</span>
      <span class="opt" style="left:95px;top:116px">Regulärer Termin</span><span class="opt" style="left:254px;top:116px">Kompakttermin</span>
      <span class="lbl" style="left:16px;top:141px">Behandelt von:</span><div class="fld" style="left:121px;top:139px;width:259px"></div>
    </div>
    <div class="form-box" style="left:38px;top:261px">
      <div class="tab">Weiterer Termin:</div>
      <span class="lbl" style="left:16px;top:20px">Datum</span><div class="fld" style="left:67px;top:18px;width:127px"></div>
      <span class="lbl" style="left:206px;top:20px">Uhrzeit</span><div class="fld" style="left:258px;top:18px;width:127px"></div>
      <div class="rule" style="top:45px"></div>
      <span class="lbl" style="left:16px;top:56px">Intervall</span>
      <span class="opt" style="left:95px;top:56px">3 Monate</span><span class="opt" style="left:229px;top:56px">6 Monate</span>
      <span class="opt" style="left:95px;top:80px">4 Monate</span><span class="opt" style="left:229px;top:80px">12 Monate</span>
      <div class="rule" style="top:106px"></div>
      <span class="lbl" style="left:16px;top:116px">Terminart</span>
      <span class="opt" style="left:95px;top:116px">Regulärer Termin</span><span class="opt" style="left:254px;top:116px">Kompakttermin</span>
      <span class="lbl" style="left:16px;top:141px">Behandelt von:</span><div class="fld" style="left:121px;top:139px;width:259px"></div>
    </div>
    <div class="form-box" style="left:38px;top:470px">
      <div class="tab">Weiterer Termin:</div>
      <span class="lbl" style="left:16px;top:20px">Datum</span><div class="fld" style="left:67px;top:18px;width:127px"></div>
      <span class="lbl" style="left:206px;top:20px">Uhrzeit</span><div class="fld" style="left:258px;top:18px;width:127px"></div>
      <div class="rule" style="top:45px"></div>
      <span class="lbl" style="left:16px;top:56px">Intervall</span>
      <span class="opt" style="left:95px;top:56px">3 Monate</span><span class="opt" style="left:229px;top:56px">6 Monate</span>
      <span class="opt" style="left:95px;top:80px">4 Monate</span><span class="opt" style="left:229px;top:80px">12 Monate</span>
      <div class="rule" style="top:106px"></div>
      <span class="lbl" style="left:16px;top:116px">Terminart</span>
      <span class="opt" style="left:95px;top:116px">Regulärer Termin</span><span class="opt" style="left:254px;top:116px">Kompakttermin</span>
      <span class="lbl" style="left:16px;top:141px">Behandelt von:</span><div class="fld" style="left:121px;top:139px;width:259px"></div>
    </div>
  </div>
</section>

<section class="page thumb" style="left:1005px;top:547px;border-color:#555">
  <div class="brand" style="top:28px">
    <span class="mark"></span>
    <span class="name">Zahnpraxis</span>
    <span class="suffix">am Lindenhof</span>
    <span class="team">Dr. Jonas &amp; Lea Brandt mit Team</span>
  </div>
  <p class="sub-title" style="left:13px;top:112px;font-size:5.6px">Öffnungszeiten</p>
  <table class="hours" style="top:127px;border-collapse:collapse">
    <tr><td>Mo:</td><td>8.00–12.30 &amp; 14.00–18.00 Uhr</td></tr>
    <tr><td>Di:</td><td>8.00–12.30 &amp; 14.00–18.00 Uhr</td></tr>
    <tr><td>Mi:</td><td>8.00–14.00 Uhr</td></tr>
    <tr><td>Do:</td><td>8.00–12.30 &amp; 14.00–18.00 Uhr</td></tr>
    <tr><td>Fr:</td><td>8.00–14.00 Uhr</td></tr>
  </table>
  <p class="sub-title" style="left:13px;top:183px;font-size:5.6px">Kontakt</p>
  <p class="hours" style="top:198px">Lindenweg 12 · 44787 Bochum<br>Tel.: 0234 – 55810<br>Praxishandy: 0176 – 28840195<br>Fax: 0234 – 558119<br>info@zahnpraxis-lindenhof.de</p>
</section>

</body>
</html>
```